Professional Coaching Business Letterhead/Footer

I need a letterhead and email footer for my personal coaching business, Dorian K Falstead Professional Coaching. I send several attachments to new clients (such as welcome letter, fee structure, etc) and would like these pages to have my branding on them.
I prefer the black and gold/silver color scheme, and will attach my logo to be used. I'd like the overall impression to be upmarket/regal/professional.

One of the uploaded files is my business card, to give an idea of the style/feel I like. The others are vector files containing logo to be used.

Target Market(s)

Corporate managers, successful business people. 30-60 yrs old.

Industry/Entity Type

Business

Requirements
Must have
• Logo (DKF)
Nice to have
• Shield emblem around logo, some type of watermark.
Should not have
• The first uploaded file is my business card, intended to show style and colors- not to be used itself as the letterhead.

```html
<!DOCTYPE html>
<html lang="en">
<head>
<meta charset="utf-8">
<title>Dorian K Falstead Professional Coaching – Letterhead</title>
<link href="https://fonts.googleapis.com/css2?family=Jost:wght@400&family=Oswald:wght@500;600&display=swap" rel="stylesheet">
<style>
  :root {
    --page-bg: #ffffff;
    --sheet-border: #050505;
    --header-bg: #ffffff;
    --ink: #111111;
    --leather-dark: #0b0b0b;
    --leather-mid: #1c1c1c;
    --gold-light: #f6c21c;
    --gold: #f0a514;
    --white: #ffffff;
  }
  * { box-sizing: border-box; margin: 0; padding: 0; }
  html, body {
    width: 1200px;
    height: 1000px;
    overflow: hidden;
    background: var(--page-bg);
  }
  .letterhead {
    position: absolute;
    left: 225px;
    top: 15px;
    width: 752px;
    height: 972px;
    border: 4px solid var(--sheet-border);
    border-radius: 6px;
    overflow: hidden;
    background: var(--leather-dark);
  }
  .letterhead__header {
    position: absolute;
    left: 0; top: 0;
    width: 100%;
    height: 174px;
    background: var(--header-bg);
  }
  .brand-mark {
    position: absolute;
    left: 50%;
    top: 24px;
    transform: translateX(-50%);
    width: 100px;
    height: 100px;
  }
  .brand-name {
    position: absolute;
    left: 0; right: 0;
    top: 131px;
    text-align: center;
    font-family: "Jost", sans-serif;
    font-weight: 400;
    font-size: 15px;
    letter-spacing: 0.3px;
    color: var(--ink);
  }
  .letterhead__body {
    position: absolute;
    left: 0; top: 174px;
    width: 100%;
    bottom: 0;
    background: radial-gradient(ellipse at 50% 45%, var(--leather-mid) 0%, #141414 45%, var(--leather-dark) 100%);
  }
  .footer {
    position: absolute;
    left: 0; right: 0;
    bottom: 0;
    height: 60px;
    font-family: "Oswald", sans-serif;
    font-weight: 600;
    text-transform: uppercase;
  }
  .footer__service {
    position: absolute;
    left: 22px;
    bottom: 14px;
    font-size: 21px;
    line-height: 1;
    letter-spacing: -0.5px;
    transform: scaleX(0.8);
    transform-origin: left bottom;
    white-space: nowrap;
  }
  .footer__service .word-a { color: var(--gold-light); }
  .footer__service .word-b { color: var(--gold); }
  .footer__divider {
    display: inline-block;
    width: 2px;
    height: 30px;
    background: var(--white);
    vertical-align: -6px;
    margin: 0 12px 0 10px;
  }
  .footer__phone { color: var(--white); }
  .footer__web {
    position: absolute;
    right: 30px;
    bottom: 9px;
    text-align: right;
    font-size: 15px;
    line-height: 18px;
    color: var(--gold);
    transform: scaleX(0.85);
    transform-origin: right bottom;
    white-space: nowrap;
  }
  .footer__web .email { text-transform: none; }
  .footer__web .email .upper { text-transform: uppercase; }
</style>
</head>
<body>
  <div class="letterhead">
    <header class="letterhead__header">
      <svg class="brand-mark" viewBox="0 0 100 100" aria-hidden="true">
        <circle cx="50" cy="50" r="46" fill="none" stroke="#111111" stroke-width="5"/>
      </svg>
      <div class="brand-name">DORIAN K FALSTEAD</div>
    </header>

    <div class="letterhead__body" role="img" aria-label="Black leather texture background"></div>

    <footer class="footer">
      <div class="footer__service">
        <span class="word-a">Professional</span> <span class="word-b">Coaching</span><span class="footer__divider"></span><span class="footer__phone">Phone : 555.014.2297</span>
      </div>
      <div class="footer__web">
        <div>DORIANKFALSTEAD.COM</div>
        <div class="email">dorian@<span class="upper">doriankfalstead.com</span></div>
      </div>
    </footer>
  </div>
</body>
</html>
```